Podiatry clinic requires a modern revamp and editing of existing website.

I would like a fresh new look and updated information for my current business website. An easy to navigate site with prominent address and phone number for call to action. We are a podiatry clinic that focuses on general and sports podiatry.
I would like 4 pages; including Home page, About Us, Services & Contact.
www.harbourlanefootcare.com

Target Market(s)

Active working professionals.

Industry/Entity Type

Medical

Coding

Coded - Design and coding required

Number of Pages Required

4 page

Font styles to use
Sans Serif

Colors
6b449b

Requirements
Must have
• A modern look with logo and active images; clean and uncluttered. Visible phone number and address for call to action.
• 4 pages - Home, About Us, Services, Contact.
• Home page - update address & service logos.
• About Us - update of personal information.
• Services - Revamp of existing page.
• Contact page to include Google map, email & phone number.
Nice to have
• Ability to add content easily; eg. a blog or adding video onto Home page.
• Link to Facebook page.

```html
<!DOCTYPE html>
<html lang="en">
<head>
<meta charset="utf-8">
<title>Harbour Lane Foot Care</title>
<link rel="stylesheet" href="https://fonts.googleapis.com/css2?family=Roboto:wght@300;400;500;700&display=swap">
<style>
:root{
  --purple:#4d3196;
  --purple-top:#5a3c9e;
  --green:#7ab829;
  --orange:#f26a21;
  --ink:#1c1c1c;
  --text:#555;
  --grey-bg:#ececec;
  --dark:#231f20;
  --line:#d6d6d6;
}
*{box-sizing:border-box;margin:0;padding:0}
html,body{width:1200px;height:2719px;overflow:hidden}
body{font-family:'Roboto',Arial,sans-serif;color:var(--text);background:#fff;position:relative}
.abs{position:absolute}
a{color:inherit;text-decoration:none}
.btn{position:absolute;background:var(--green);color:#fff;font-size:11px;display:flex;align-items:center;justify-content:center}

/* top bar */
.topbar{left:0;top:0;width:1200px;height:38px;background:var(--purple-top);color:#fff;font-size:11px}
.topbar .item{position:absolute;top:0;height:38px;display:flex;align-items:center;gap:8px}
.topbar svg{fill:var(--green)}
.book{left:892px;top:0;width:176px;height:38px;font-size:12px}

/* header */
.header{left:0;top:38px;width:1200px;height:105px;background:#fff}
.logo{left:132px;top:12px;display:flex;align-items:center;gap:10px;height:80px}
.logo .dot{width:20px;height:20px;border-radius:50%;background:var(--purple)}
.logo span{font-size:24px;font-weight:500;color:var(--purple);line-height:1.05;width:140px}
.nav{left:386px;top:0;height:105px;display:flex;align-items:center;gap:24px;font-size:12px;color:#333}
.nav .active{position:relative}
.nav .active::after{content:"";position:absolute;left:-8px;right:-8px;top:-27px;height:2px;background:var(--orange)}
.nav .active::before{content:"";position:absolute;left:-8px;right:-8px;top:20px;height:2px;background:var(--orange)}

/* hero */
.hero{left:0;top:143px;width:1200px;height:448px;background:linear-gradient(180deg,#6f7168 0%,#3e3f3a 45%,#4a4a46 100%)}
.hero h1{position:absolute;left:0;width:1200px;top:122px;text-align:center;color:#fff;font-size:36px;font-weight:500}
.hero p{position:absolute;left:0;width:1200px;top:172px;text-align:center;color:#fff;font-size:18px;line-height:24px}
.hero p em{font-style:italic}
.hero .btn{left:551px;top:249px;width:96px;height:30px}
.hero .arrow{position:absolute;top:210px}

/* section titles */
.rule{position:absolute;width:46px;height:2px;background:var(--orange)}

/* about */
.about h2{left:132px;top:632px;font-size:24px;font-weight:500;color:var(--ink)}
.about .txt{left:132px;top:691px;width:406px;font-size:10.5px;line-height:14px;color:#555}
.about .txt p{margin-bottom:9px}
.vdivider{position:absolute;width:2px;background:var(--line)}
.video{left:611px;top:640px;width:457px;height:261px;background:linear-gradient(135deg,#e9ecef 0%,#c5ccd3 50%,#dcd4ce 100%)}
.play{left:818px;top:756px;width:36px;height:26px;background:#e52d27;border-radius:6px}

/* treatments */
.treat{left:0;top:937px;width:1200px;height:486px;background:var(--purple)}
.treat h2{position:absolute;left:0;width:1200px;top:42px;text-align:center;color:#fff;font-size:23px;font-weight:500}
.tab{position:absolute;top:114px;height:35px;border-radius:18px;color:#fff;font-size:14px;display:flex;align-items:center;justify-content:center}
.tab.on{left:384px;width:203px;background:var(--green)}
.tab.off{left:613px;width:203px;border:1.5px solid #fff}
.tline{position:absolute;top:131px;height:1px;background:#8a76c0}
.circ{position:absolute;top:120px;width:24px;height:24px;border-radius:50%;background:#9283c4;display:flex;align-items:center;justify-content:center}
.card{position:absolute;top:172px;width:216px;color:#fff}
.card .ph{height:147px}
.card h3{font-size:19px;font-weight:400;margin-top:14px}
.card p{font-size:10.5px;line-height:14px;margin-top:4px}
.card .more{font-size:10px;margin-top:14px;display:block}

/* products */
.pgrid{left:132px;top:1472px;width:455px;height:261px}
.pgrid div{position:absolute}
.prod h2{left:665px;top:1468px;font-size:23px;font-weight:500;color:var(--ink)}
.prod .txt{left:665px;top:1527px;width:403px;font-size:10.5px;line-height:14px;color:#555}
.prod .txt p{margin-bottom:8px}

/* blog */
.blog{left:0;top:1782px;width:1200px;height:536px;background:var(--grey-bg)}
.blog h2{position:absolute;left:0;width:1200px;top:42px;text-align:center;font-size:28px;font-weight:400;color:var(--ink)}
.blog .sub{position:absolute;left:0;width:1200px;top:80px;text-align:center;font-size:13px;color:#555}
.post{position:absolute;top:136px;width:296px;height:362px;background:#fff}
.post .ph{height:121px}
.post .body{padding:24px 24px 0}
.post .date{font-size:11px;color:var(--purple)}
.post h3{font-size:14px;font-weight:400;color:var(--ink);line-height:19px;margin-top:8px}
.post hr{border:0;border-top:1px solid #e2e2e2;margin:14px 0 12px}
.post p{font-size:10.5px;line-height:14.5px;color:#555}
.post .more{display:block;font-size:10.5px;color:#444;margin-top:24px}

/* partners */
.pcirc{position:absolute;top:2383px;width:32px;height:32px;border-radius:50%;background:#555;display:flex;align-items:center;justify-content:center}
.badge{position:absolute;top:2366px;width:170px;height:65px;border:1px solid #e0e0e0;background:#fff}
.badge i{position:absolute;left:35px;top:18px;width:100px;height:28px;border-radius:4px}

/* footer */
.footer{left:0;top:2478px;width:1200px;height:196px;background:var(--dark);color:#fff}
.fcol{position:absolute;top:0;height:196px;display:flex;flex-direction:column;align-items:center;justify-content:center;text-align:center;font-size:12.5px;line-height:18px}
.fcol svg{fill:#fff;margin-bottom:14px}
.fcol .big{font-size:19px;line-height:24px}
.fcol u{text-decoration:underline}
.fdiv{position:absolute;top:30px;width:1px;height:136px;background:#555}
.bottombar{left:0;top:2674px;width:1200px;height:45px;background:var(--purple);color:#fff;font-size:11px}
.social{position:absolute;left:1037px;top:11px;width:24px;height:24px;background:#fff}
</style>
</head>
<body>

<div class="abs topbar">
  <div class="item" style="left:140px">
    <svg width="10" height="13" viewBox="0 0 10 13"><path d="M5 0a5 5 0 0 0-5 5c0 3.5 5 8 5 8s5-4.5 5-8a5 5 0 0 0-5-5zm0 7a2 2 0 1 1 0-4 2 2 0 0 1 0 4z"/></svg>
    Suite 214 / 62 Harbour Lane Melbourne 3000
  </div>
  <div class="item" style="left:402px">
    <svg width="12" height="12" viewBox="0 0 24 24"><path d="M6.6 10.8a15 15 0 0 0 6.6 6.6l2.2-2.2a1 1 0 0 1 1-.25 11.4 11.4 0 0 0 3.6.57 1 1 0 0 1 1 1V20a1 1 0 0 1-1 1A17 17 0 0 1 3 4a1 1 0 0 1 1-1h3.5a1 1 0 0 1 1 1c0 1.25.2 2.45.57 3.57a1 1 0 0 1-.25 1z"/></svg>
    1300 482 905
  </div>
  <div class="item" style="left:518px">
    <svg width="13" height="10" viewBox="0 0 13 10"><path d="M0 0h13v10H0z M1 1l5.5 4.5L12 1z" fill-rule="evenodd"/></svg>
    info@harbourlanefootcare.com
  </div>
  <a class="btn book">Book An Appointment</a>
</div>

<header class="abs header">
  <div class="abs logo"><div class="dot"></div><span>Harbour Lane Foot Care</span></div>
  <nav class="abs nav">
    <a class="active">About Us</a>
    <a>Podiatry Treatments</a>
    <a>Podiatry Products &amp; Footwear</a>
    <a>Health &amp; Wellness Products</a>
    <a>Contact Us</a>
  </nav>
</header>

<section class="abs hero" role="img" aria-label="Photo of runners' legs and shoes on a sunlit path">
  <svg class="arrow" style="left:84px" width="14" height="24" viewBox="0 0 14 24"><path d="M12 2 2 12l10 10" stroke="#fff" stroke-width="2.5" fill="none"/></svg>
  <svg class="arrow" style="left:1102px" width="14" height="24" viewBox="0 0 14 24"><path d="m2 2 10 10L2 22" stroke="var(--green)" stroke-width="2.5" fill="none"/></svg>
  <h1>Harbour Lane Foot Care</h1>
  <p>We provide General Podiatry Treatment and some Specialised&nbsp; Services in relation to various<br><em>foot conditions, including Sports Injuries,&nbsp; Orthotic Therapy and Nail Surgery.</em></p>
  <a class="btn">View All</a>
</section>

<section class="about">
  <h2 class="abs">About Us</h2>
  <div class="rule" style="left:132px;top:672px"></div>
  <div class="abs txt">
    <p>Harbour Lane Foot Care is a Podiatry clinic in the heart of Melbourne CBD. We are located between Bay &amp; Quarry Streets in the Harbourside Business Centre.</p>
    <p>Our podiatrists are fully qualified health professionals who are able to diagnose, treat, manage or help to prevent all medical&nbsp; conditions that affect the feet and lower limb.</p>
    <p>We provide General Podiatry Treatment and some Specialised Services in relation to various foot conditions, including Sports Injuries, Orthotic Therapy and Nail Surgery.</p>
  </div>
  <a class="btn" style="left:132px;top:872px;width:109px;height:29px">Discover More</a>
  <div class="vdivider" style="left:572px;top:640px;height:261px"></div>
  <div class="abs video" role="img" aria-label="Video still of a podiatrist treating a foot under a magnifying lamp"></div>
  <div class="abs play"><svg width="36" height="26" viewBox="0 0 36 26"><path d="M14 7v12l10-6z" fill="#fff"/></svg></div>
</section>

<section class="abs treat">
  <h2>Podiatry Treatments</h2>
  <div class="rule" style="left:577px;top:88px"></div>
  <div class="tline" style="left:132px;width:252px"></div>
  <div class="tline" style="left:816px;width:252px"></div>
  <div class="circ" style="left:233px"><svg width="8" height="10" viewBox="0 0 8 10"><path d="M6 1 2 5l4 4" stroke="#fff" stroke-width="1.6" fill="none"/></svg></div>
  <div class="circ" style="left:941px"><svg width="8" height="10" viewBox="0 0 8 10"><path d="m2 1 4 4-4 4" stroke="#fff" stroke-width="1.6" fill="none"/></svg></div>
  <div class="tab on">General Treatments</div>
  <div class="tab off">Specialised Treatments</div>

  <div class="card" style="left:132px">
    <div class="ph" role="img" aria-label="Photo of toenail care" style="background:linear-gradient(135deg,#8fd3dc,#e8c9b8)"></div>
    <h3>Nails</h3><p>Ipum passages, and more recently with desktop publishing like.</p><a class="more">Read More ...</a>
  </div>
  <div class="card" style="left:372px">
    <div class="ph" role="img" aria-label="Photo of corn treatment with a file" style="background:linear-gradient(135deg,#d9cfc4,#c79c85)"></div>
    <h3>Corns</h3><p>Ipum passages, and more recently with desktop publishing like.</p><a class="more" style="color:var(--green)">Read More ...</a>
  </div>
  <div class="card" style="left:613px">
    <div class="ph" role="img" aria-label="Photo of callus removal with a scalpel" style="background:linear-gradient(135deg,#3a3030,#c98f72)"></div>
    <h3>Callus</h3><p>Ipum passages, and more recently with desktop publishing like.</p><a class="more">Read More ...</a>
  </div>
  <div class="card" style="left:852px">
    <div class="ph" role="img" aria-label="Photo of wart treatment on a foot" style="background:linear-gradient(135deg,#6b5a55,#e6cdbf)"></div>
    <h3>Warts</h3><p>Ipum passages, and more recently with desktop publishing like.</p><a class="more">Read More ...</a>
  </div>
</section>

<section class="prod">
  <div class="abs pgrid">
    <div role="img" aria-label="Photo of foot cream jars" style="left:0;top:0;width:228px;height:131px;background:linear-gradient(135deg,#f4f1e6,#e9c46a)"></div>
    <div role="img" aria-label="Photo of toe separators and gel pads" style="left:228px;top:0;width:227px;height:131px;background:linear-gradient(135deg,#d9d9d6,#e2c2ae)"></div>
    <div role="img" aria-label="Photo of shoes on a display shelf" style="left:0;top:131px;width:228px;height:130px;background:linear-gradient(135deg,#b7ad9f,#3b3a38)"></div>
    <div role="img" aria-label="Photo of a skin cream box" style="left:228px;top:131px;width:227px;height:130px;background:linear-gradient(135deg,#eae7e2,#6f9bc6)"></div>
  </div>
  <div class="vdivider" style="left:624px;top:1472px;height:261px"></div>
  <h2 class="abs">Podiatry Product &amp; Footwear</h2>
  <div class="rule" style="left:665px;top:1508px"></div>
  <div class="abs txt">
    <p>In enim justo, rhoncus ut, imperdiet a, venenatis vitae, justo. Nullam dictum felis eu pede mollis pretium. Integer tincidunt. Cras dapibus. Vivamus elementum semper nisi. Aenean vulputate eleifend tellus. Aenean leo ligula, porttitor eu, consequat vitae, eleifend ac, enim.</p>
    <p>Aliquam lorem ante, dapibus in, viverra quis, feugiat a, tellus. Phasellus viverra nulla ut metus varius laoreet. Quisque rutrum. Aenean imperdiet. Etiam ultricies nisi vel augue. Curabitur ullamcorper ultricies nisi. Nam eget dui. Etiam</p>
  </div>
  <a class="btn" style="left:663px;top:1704px;width:113px;height:31px">Explore More</a>
</section>

<section class="abs blog">
  <h2>We make your life easy. Here’s how.</h2>
  <div class="sub">Check out our recently posted articles.</div>
  <div class="rule" style="left:577px;top:106px"></div>

  <article class="post" style="left:132px">
    <div class="ph" role="img" aria-label="Photo of marathon runners' legs on a road" style="background:linear-gradient(180deg,#9a9a98,#5f5e5b)"></div>
    <div class="body"><div class="date">Des 7th, 2016</div><h3>Established fact that a reader will be distracted</h3><hr><p>It is a long established fact that a reader will be distracted by the readable content of a page when looking at its layout will be distracted by the readable&nbsp; ...</p><a class="more">Read More ...</a></div>
  </article>
  <article class="post" style="left:451px">
    <div class="ph" role="img" aria-label="Photo of runners' colourful shoes on a track" style="background:linear-gradient(180deg,#7f8f88,#4d5c5a)"></div>
    <div class="body"><div class="date">Des 7th, 2016</div><h3>Established fact that a reader will be distracted</h3><hr><p>It is a long established fact that a reader will be distracted by the readable content of a page when looking at its layout will be distracted by the readable&nbsp; ...</p><a class="more">Read More ...</a></div>
  </article>
  <article class="post" style="left:772px">
    <div class="ph" role="img" aria-label="Photo of a sprinter's feet at the start line" style="background:linear-gradient(180deg,#f1ece8,#c0553b)"></div>
    <div class="body"><div class="date">Des 7th, 2016</div><h3>Established fact that a reader will be distracted</h3><hr><p>It is a long established fact that a reader will be distracted by the readable content of a page when looking at its layout will be distracted by the readable&nbsp; ...</p><a class="more">Read More ...</a></div>
  </article>
</section>

<section class="partners">
  <div class="pcirc" style="left:84px"><svg width="8" height="12" viewBox="0 0 8 12"><path d="M6 1 1 6l5 5" stroke="#fff" stroke-width="1.8" fill="none"/></svg></div>
  <div class="pcirc" style="left:1084px"><svg width="8" height="12" viewBox="0 0 8 12"><path d="m2 1 5 5-5 5" stroke="#fff" stroke-width="1.8" fill="none"/></svg></div>
  <div class="badge" style="left:132px"><i style="background:#5aa640"></i></div>
  <div class="badge" style="left:323px"><i style="background:#2d4a9a"></i></div>
  <div class="badge" style="left:515px"><i style="background:#f0a81c"></i></div>
  <div class="badge" style="left:707px"><i style="background:#2b2b2b"></i></div>
  <div class="badge" style="left:899px"><i style="background:#1f3f95;left:65px;width:40px"></i></div>
</section>

<footer class="abs footer">
  <div class="fcol" style="left:132px;width:316px">
    <svg width="16" height="22" viewBox="0 0 10 13"><path d="M5 0a5 5 0 0 0-5 5c0 3.5 5 8 5 8s5-4.5 5-8a5 5 0 0 0-5-5zm0 7a2 2 0 1 1 0-4 2 2 0 0 1 0 4z"/></svg>
    Suite 214 / 62 Harbour Lane<br>Melbourne 3000.
  </div>
  <div class="fdiv" style="left:448px"></div>
  <div class="fcol" style="left:449px;width:320px">
    <svg width="22" height="22" viewBox="0 0 24 24"><path d="M6.6 10.8a15 15 0 0 0 6.6 6.6l2.2-2.2a1 1 0 0 1 1-.25 11.4 11.4 0 0 0 3.6.57 1 1 0 0 1 1 1V20a1 1 0 0 1-1 1A17 17 0 0 1 3 4a1 1 0 0 1 1-1h3.5a1 1 0 0 1 1 1c0 1.25.2 2.45.57 3.57a1 1 0 0 1-.25 1z"/></svg>
    <span class="big">1300 482 905</span>
    info@harbourlanefootcare.com
  </div>
  <div class="fdiv" style="left:769px"></div>
  <div class="fcol" style="left:770px;width:298px">
    <span style="font-size:24px;font-weight:700;margin-bottom:10px">?</span>
    Have a Question?<br><u>Contact Us</u>
  </div>
</footer>

<div class="abs bottombar">
  <div class="abs" style="left:132px;top:15px">©2016, harbourlanefootcare.com</div>
  <div class="abs" style="left:960px;top:14px;font-size:13px">Follow Us</div>
  <div class="social"></div>
</div>

</body>
</html>
```